design an app for runners to engage them in collective challenges

Creative Brief: Running Application - Collective Challenges
Objective
To design a simple yet impactful mobile application for runners, centered around collective challenges. The app should offer an engaging, user-friendly experience while encouraging participation in running challenges. Starting with a minimalist and robust version, the design must focus on essential features, allowing for future enhancements as the user base grows.

Target Audience
Primary Users: Casual to dedicated runners who enjoy tracking their progress and participating in challenges.
Motivations: Community-driven goals, personal achievements, and tangible rewards.
Needs: A visually appealing, straightforward interface with real-time progress tracking and clear challenge objectives.
Core Features
Main Screen: Current Challenge

Displays the active challenge with a title, visual, prize description, and countdown for kilometers remaining.
Prominent “Join” button for easy participation.
Quick access to challenge conditions (eg, most kilometers, fastest pace, random draw).
Challenge Details

Includes challenge rules, detailed prize information, and victory conditions.
Simplified text for clarity and engagement.
Past Challenges

Showcases previous challenges, total kilometers achieved, and winners.
Admin Section

Enables challenge creation with scheduling, descriptions, and victory criteria.
Minimalist design for ease of use.
Look and Feel
Visual Identity: Clean, modern, and energetic design reflecting the spirit of running and collective achievement.
Color Palette:
Vibrant primary colors: Blue and green for energy and motivation.
Accent colors: Orange or yellow for highlights, paired with a dark background for strong contrast.
Typography:
Sans-serif fonts like Lato or Montserrat for readability.
Bold, prominent numbers for key statistics like kilometers completed.
Icons and Graphics:
Minimalistic icons with light, functional animations (eg, a moving kilometer counter).
Clear, motivational visuals to support collective progress.
Tone and Style
Tone: Encouraging, community-focused, and goal-oriented.
Style: Minimalistic with a focus on clarity and user engagement.
References
Inspirations:
Velta Stride Circle for its simplicity and modern interface.
Quorvo for its community features and tracking precision.
Deliverables
Wireframes and UI designs for all key screens: login, current challenge, challenge details, past challenges, and admin panel.
Visual assets: icons, buttons, and animations.
A consistent design system to ensure scalability for future features.
Updates

Target Market(s)

Casual to dedicated runners who enjoy tracking their progress and participating in challenges.

Industry/Entity Type

sport

Font styles to use
Sans Serif

Colors

Designer to choose colors to be used in the design.

Requirements
Must have
• to design all screens

```html
<!DOCTYPE html>
<html lang="en">
<head>
<meta charset="utf-8">
<title>Runner Challenges – App Screens</title>
<link href="https://fonts.googleapis.com/css2?family=Lexend:wght@400;500;600;700&family=Inter:wght@400;500;600&display=swap" rel="stylesheet">
<style>
:root{
  --bg:#e4e4e3;
  --screen:#ffffff;
  --tile:#eeefeb;
  --green:#a0ee10;
  --dark:#3a3a3a;
  --ink:#161616;
  --muted:#555;
  --accent:#f4d80c;
  --photo-a:#6d5a48;
  --photo-b:#b59a70;
}
*{box-sizing:border-box;margin:0;padding:0}
html,body{width:873px;height:1200px;overflow:hidden;background:var(--bg)}
body{font-family:"Inter",sans-serif;color:var(--ink)}
.board{position:absolute;left:0;top:0;width:1600px;height:2200px;transform:scale(0.545625);transform-origin:0 0}
.screen{position:absolute;width:402px;height:874px;background:var(--screen);border-radius:50px;overflow:hidden}
.screen *{position:absolute}
.caption{position:absolute;width:402px;text-align:center;font-size:11px;letter-spacing:.3px;color:#333;font-family:"Inter",sans-serif}
.time{left:55px;top:20px;font:500 16px "Inter",sans-serif}
.status{right:40px;top:22px}
.home-bar{left:110px;bottom:10px;width:184px;height:4px;border-radius:2px;background:var(--ink)}
.lbl{font:400 11px "Inter",sans-serif;letter-spacing:.3px;color:#444}
.big{font:600 34px "Lexend",sans-serif;line-height:1;color:var(--ink)}
.unit{font:500 11px "Lexend",sans-serif;color:var(--ink)}
.tile{background:var(--tile);border-radius:22px}
.green{background:var(--green);border-radius:22px;overflow:hidden}
.title{font:600 23px "Lexend",sans-serif;line-height:29px;color:var(--ink)}
.photo{background:linear-gradient(135deg,var(--photo-a),var(--photo-b) 60%,#3b3f52)}
.pill{border-radius:22px}
.back{left:16px;top:70px;width:56px;height:40px;background:var(--tile);border-radius:20px}
.back svg{left:14px;top:12px}
.dark-bar{left:8px;width:386px;height:66px;background:var(--dark);border-radius:22px}
.dark-bar .join{font:600 14px "Lexend",sans-serif;color:var(--accent);text-align:right;line-height:17px}
.dark-bar .go{width:56px;height:40px;border:1.5px solid var(--accent);border-radius:20px;top:13px;right:18px}
.dark-bar .go svg{left:20px;top:12px}
.dark-bar .big{color:#fff}
.dark-bar .unit{color:#fff;font-size:14px;line-height:14px}
.dark-bar .sub{color:#fff;font:400 11px "Inter",sans-serif;letter-spacing:.3px}
.share{right:8px;top:69px;width:113px;height:42px;background:var(--dark);border-radius:21px}
.share span{left:16px;top:13px;font:600 13px "Lexend",sans-serif;color:var(--accent)}
.share svg{right:10px;top:10px}
.participants{top:76px;font:600 24px "Lexend",sans-serif}
.participants small{position:static;font:500 12px "Lexend",sans-serif;margin-left:6px}
.live{background:rgba(255,255,255,.72);border-radius:20px;height:38px;font:500 12px "Lexend",sans-serif}
</style>
</head>
<body>
<div class="board">

<svg width="0" height="0" style="position:absolute">
  <defs>
    <symbol id="i-status" viewBox="0 0 80 14"><rect x="0" y="9" width="3" height="5" rx="1"/><rect x="5" y="6" width="3" height="8" rx="1"/><rect x="10" y="3" width="3" height="11" rx="1"/><rect x="15" y="0" width="3" height="14" rx="1"/><path d="M30 5a11 11 0 0 1 15 0l-2 2a8 8 0 0 0-11 0zM33 8a6 6 0 0 1 9 0l-4.5 5z"/><rect x="53" y="2" width="24" height="11" rx="3"/><rect x="78" y="5" width="2" height="5" rx="1"/></symbol>
    <symbol id="i-route" viewBox="0 0 24 24" fill="none" stroke="currentColor" stroke-width="1.6"><circle cx="6" cy="5" r="3"/><circle cx="18" cy="19" r="3"/><path d="M6 8v3a3 3 0 0 0 3 3h6a3 3 0 0 1 3 3" /><path d="M3 21h7"/></symbol>
    <symbol id="i-gauge" viewBox="0 0 24 24" fill="none" stroke="currentColor" stroke-width="1.6"><circle cx="12" cy="12" r="9"/><path d="M12 12l4-4"/></symbol>
    <symbol id="i-wave" viewBox="0 0 24 24" fill="none" stroke="currentColor" stroke-width="1.6"><path d="M2 12c3-5 5-5 8 0s5 5 8 0 3-2 4-2"/><path d="M2 17c3-4 5-4 8 0"/></symbol>
    <symbol id="i-cal" viewBox="0 0 24 24" fill="none" stroke="currentColor" stroke-width="1.6"><rect x="3" y="5" width="18" height="16" rx="3"/><path d="M3 10h18M8 3v4M16 3v4"/><rect x="14" y="14" width="3" height="3"/></symbol>
    <symbol id="i-clock" viewBox="0 0 24 24" fill="none" stroke="currentColor" stroke-width="1.6"><circle cx="12" cy="12" r="9"/><path d="M12 7v5l-3 3"/></symbol>
    <symbol id="i-timer" viewBox="0 0 24 24" fill="none" stroke="currentColor" stroke-width="1.6"><circle cx="12" cy="13" r="8"/><path d="M12 9v4M9 3h6"/></symbol>
    <symbol id="i-trophy" viewBox="0 0 24 24" fill="none" stroke="currentColor" stroke-width="1.6"><path d="M7 3h10v6a5 5 0 0 1-10 0zM7 5H3v2a4 4 0 0 0 4 4M17 5h4v2a4 4 0 0 1-4 4M12 14v4M8 21h8l-1-3H9z"/></symbol>
    <symbol id="i-flag" viewBox="0 0 24 24"><path d="M2 5h4v4H2zM10 5h4v4h-4zM18 5h4v4h-4zM6 9h4v4H6zM14 9h4v4h-4zM2 13h4v4H2zM10 13h4v4h-4zM18 13h4v4h-4z"/></symbol>
    <symbol id="i-map" viewBox="0 0 24 24" fill="none" stroke="currentColor" stroke-width="1.6"><path d="M3 6l5-2 8 3 5-2v13l-5 2-8-3-5 2z"/></symbol>
    <symbol id="i-pin" viewBox="0 0 24 24" fill="none" stroke="currentColor" stroke-width="1.6"><path d="M12 22s7-7 7-12a7 7 0 0 0-14 0c0 5 7 12 7 12z"/><circle cx="12" cy="10" r="2.5"/></symbol>
    <symbol id="i-share" viewBox="0 0 24 24" fill="none" stroke="currentColor" stroke-width="1.6"><circle cx="12" cy="5" r="3"/><circle cx="5" cy="18" r="3"/><circle cx="19" cy="18" r="3"/><path d="M10 8l-3 7M14 8l3 7M8 18h8"/></symbol>
    <symbol id="i-chev" viewBox="0 0 12 12" fill="none" stroke="currentColor" stroke-width="1.6"><path d="M4 2l4 4-4 4"/></symbol>
    <symbol id="i-back" viewBox="0 0 12 12" fill="none" stroke="currentColor" stroke-width="1.6"><path d="M8 2L4 6l4 4"/></symbol>
    <symbol id="i-up" viewBox="0 0 12 12" fill="none" stroke="currentColor" stroke-width="1.6"><path d="M2 8l4-4 4 4"/></symbol>
    <symbol id="i-addtimer" viewBox="0 0 24 24" fill="none" stroke="currentColor" stroke-width="1.6"><circle cx="12" cy="13" r="8"/><path d="M12 10v6M9 13h6M4 5l3-2M20 5l-3-2"/></symbol>
    <symbol id="i-home" viewBox="0 0 24 24" fill="none" stroke="currentColor" stroke-width="1.6"><path d="M4 10l8-6 8 6v10H4zM10 20v-5h4v5"/></symbol>
    <symbol id="i-sliders" viewBox="0 0 24 24" fill="none" stroke="currentColor" stroke-width="1.6"><path d="M3 8h18M3 16h18"/><circle cx="9" cy="8" r="2.5" fill="#fff"/><circle cx="15" cy="16" r="2.5" fill="#fff"/></symbol>
    <symbol id="i-upload" viewBox="0 0 24 24" fill="none" stroke="currentColor" stroke-width="1.6"><path d="M12 15V4M7 9l5-5 5 5M4 15v3a3 3 0 0 0 3 3h10a3 3 0 0 0 3-3v-3"/></symbol>
    <symbol id="i-plus" viewBox="0 0 24 24" fill="none" stroke="currentColor" stroke-width="1.6"><path d="M12 3v18M3 12h18"/></symbol>
    <symbol id="i-x" viewBox="0 0 12 12" fill="none" stroke="currentColor" stroke-width="1.4"><path d="M2 2l8 8M10 2l-8 8"/></symbol>
  </defs>
</svg>

<!-- ============ MY CHALLENGES ============ -->
<section class="screen" style="left:338px;top:120px">
  <div class="time">9:41</div>
  <svg class="status" width="80" height="14" fill="#111"><use href="#i-status"/></svg>

  <div class="segmented" style="left:8px;top:64px;width:386px;height:64px;background:var(--tile);border-radius:32px">
    <span style="left:38px;top:25px;font:500 12.5px 'Lexend',sans-serif">PAST CHALLENGES</span>
    <div style="left:193px;top:8px;width:185px;height:48px;background:var(--dark);border-radius:24px">
      <span style="left:0;right:0;top:17px;text-align:center;font:500 12.5px 'Lexend',sans-serif;color:var(--accent)">MY CHALLENGES</span>
    </div>
  </div>
  <div class="filter" style="left:338px;top:136px;width:56px;height:40px;background:var(--tile);border-radius:20px">
    <svg style="left:20px;top:13px" width="16" height="14" stroke="#222" stroke-width="1.6"><path d="M2 5h12M5 10h6"/></svg>
  </div>

  <!-- card 1 -->
  <div class="green challenge-card" style="left:8px;top:182px;width:386px;height:192px">
    <div class="photo" role="img" aria-label="Marathon runner in a yellow vest" style="left:0;top:0;width:386px;height:192px;clip-path:polygon(270px 0,386px 0,386px 192px,200px 192px)"></div>
    <div class="title" style="left:32px;top:24px;width:200px">Downtown Up &amp; Running II</div>
    <svg style="left:32px;top:96px" width="24" height="24" color="#111"><use href="#i-trophy"/></svg>
    <div style="left:32px;top:137px;font:400 13px 'Inter',sans-serif;line-height:16px;width:180px">6 Month Free Pulse Club Subscription</div>
    <div class="live" style="left:234px;top:146px;width:144px"><span style="left:12px;top:12px">LIVE STATS</span><svg style="right:12px;top:13px" width="12" height="12" color="#111"><use href="#i-up"/></svg></div>
  </div>
  <div class="tile stats" style="left:8px;top:376px;width:386px;height:116px;border-radius:8px 8px 22px 22px">
    <svg style="left:24px;top:16px" width="24" height="24" color="#111"><use href="#i-route"/></svg>
    <div class="big" style="left:24px;top:44px">3</div><div class="unit" style="left:52px;top:46px">KM</div>
    <div class="lbl" style="left:24px;top:89px">TOTAL DISTANCE</div>
    <svg style="left:142px;top:16px" width="24" height="24" color="#111"><use href="#i-gauge"/></svg>
    <div class="big" style="left:142px;top:44px">29</div><div class="unit" style="left:192px;top:46px">KM/H</div>
    <div class="lbl" style="left:142px;top:89px">AVERAGE SPEED</div>
    <svg style="left:279px;top:16px" width="24" height="24" color="#111"><use href="#i-wave"/></svg>
    <div class="big" style="left:279px;top:44px">30</div><div class="unit" style="left:332px;top:46px">KM/H</div>
    <div class="lbl" style="left:279px;top:89px">HIGHEST SPEED</div>
  </div>
  <div class="dark-bar" style="top:496px">
    <svg style="left:24px;top:21px" width="24" height="24" color="#fff"><use href="#i-timer"/></svg>
    <div class="big" style="left:50px;top:17px">1.3</div>
    <div class="unit" style="left:108px;top:18px">KM</div>
    <div class="sub" style="left:108px;top:36px">REMAINING</div>
    <div class="join" style="right:86px;top:15px">JOIN THE<br>CHALLENGE</div>
    <div class="go"><svg width="12" height="12" color="var(--accent)"><use href="#i-chev"/></svg></div>
  </div>

  <!-- card 2 -->
  <div class="green challenge-card" style="left:8px;top:593px;width:386px;height:192px">
    <div class="photo" role="img" aria-label="Female runner in a blue race top" style="left:0;top:0;width:386px;height:192px;clip-path:polygon(270px 0,386px 0,386px 192px,200px 192px);background:linear-gradient(135deg,#c9a78a,#3d63b8 55%,#e4e0da)"></div>
    <div class="title" style="left:32px;top:24px;width:200px">Downtown Up &amp; Running II</div>
    <svg style="left:32px;top:96px" width="24" height="24" color="#111"><use href="#i-trophy"/></svg>
    <div style="left:32px;top:137px;font:400 13px 'Inter',sans-serif;line-height:16px;width:180px">6 Month Free Pulse Club Subscription</div>
    <div class="live" style="left:234px;top:146px;width:144px"><span style="left:12px;top:12px">LIVE STATS</span></div>
    <div style="left:302px;top:117px;width:70px;height:54px;background:var(--green);border-radius:16px">
      <svg style="left:23px;top:15px" width="24" height="24" color="#111"><use href="#i-addtimer"/></svg>
    </div>
  </div>
  <div class="ghost-stats" style="left:32px;top:828px;opacity:.25;width:360px;height:40px">
    <div class="big" style="left:0;top:0">3</div><div class="big" style="left:118px;top:0">29</div><div class="big" style="left:255px;top:0">30</div>
  </div>
  <nav class="tabbar" style="left:8px;top:788px;width:386px;height:54px;background:rgba(238,239,235,.92);border-radius:22px">
    <svg style="left:34px;top:15px" width="24" height="24" color="#777"><use href="#i-home"/></svg>
    <div style="left:86px;top:4px;width:142px;height:46px;background:var(--dark);border-radius:23px">
      <span style="left:12px;top:16px;font:500 10.5px 'Lexend',sans-serif;color:var(--accent)">MY CHALLANGES</span>
      <svg style="left:108px;top:14px" width="20" height="18" fill="var(--accent)"><use href="#i-flag"/></svg>
    </div>
    <svg style="left:256px;top:15px" width="24" height="24" color="#777"><use href="#i-sliders"/></svg>
    <svg style="left:328px;top:15px" width="24" height="24" color="#777"><use href="#i-addtimer"/></svg>
  </nav>
  <div class="home-bar"></div>
</section>
<div class="caption" style="left:338px;top:1027px">MY CHALLANGES</div>

<!-- ============ CREATE CHALLENGE ============ -->
<section class="screen" style="left:860px;top:120px">
  <div class="time">9:41</div>
  <svg class="status" width="80" height="14" fill="#111"><use href="#i-status"/></svg>
  <div class="back"><svg width="12" height="12" color="#111"><use href="#i-back"/></svg></div>
  <div style="left:0;right:0;top:82px;text-align:center;font:600 14px 'Lexend',sans-serif">NEW CHALLANGE</div>

  <div class="lbl" style="left:16px;top:125px">EVENT PHOTO (OPTIONAL)</div>
  <div class="photo" role="img" aria-label="Group of runners' legs on a race road" style="left:8px;top:152px;width:386px;height:192px;border-radius:22px;clip-path:polygon(0 0,386px 0,300px 192px,0 192px);background:linear-gradient(135deg,#8d6e5a,#d9c1a3 50%,#5d4a40)"></div>
  <div class="pill" style="left:250px;top:292px;width:142px;height:38px;background:rgba(255,255,255,.9)">
    <span style="left:8px;top:12px;font:500 12px 'Lexend',sans-serif">UPLOAD PHOTO</span>
    <svg style="right:12px;top:8px" width="22" height="22" color="#111"><use href="#i-upload"/></svg>
  </div>

  <div class="lbl" style="left:16px;top:365px">EVENT TITLE</div>
  <div class="green" style="left:8px;top:393px;width:386px;height:79px">
    <div class="title" style="left:24px;top:12px;width:320px">Downtown Up &amp; Running 3KM</div>
  </div>

  <div class="lbl" style="left:16px;top:501px">TIME AND DATE</div>
  <div class="tile" style="left:8px;top:528px;width:120px;height:120px">
    <svg style="left:24px;top:18px" width="24" height="24" color="#111"><use href="#i-cal"/></svg>
    <div class="big" style="left:24px;top:46px">25</div><div class="unit" style="left:75px;top:50px">NOV</div>
    <div class="lbl" style="left:24px;top:91px">EVENT DATE</div>
  </div>
  <div class="tile" style="left:141px;top:528px;width:120px;height:120px">
    <svg style="left:24px;top:18px" width="24" height="24" color="#111"><use href="#i-clock"/></svg>
    <div class="big" style="left:24px;top:46px">9:00</div>
    <div class="lbl" style="left:24px;top:91px">START TIME</div>
  </div>
  <div class="tile" style="left:274px;top:528px;width:120px;height:120px">
    <svg style="left:24px;top:18px" width="24" height="24" color="#111"><use href="#i-plus"/></svg>
    <div class="big" style="left:24px;top:46px">1</div><div class="unit" style="left:46px;top:50px">DAY</div>
    <div class="lbl" style="left:24px;top:91px">ADD MORE</div>
  </div>

  <div class="lbl" style="left:16px;top:677px">AREA AND DISTANCE</div>
  <div class="tile" style="left:8px;top:704px;width:120px;height:110px">
    <svg style="left:24px;top:20px" width="24" height="24" color="#111"><use href="#i-map"/></svg>
    <div style="left:24px;top:48px;font:600 24px 'Lexend',sans-serif">Start</div>
  </div>
  <div class="tile" style="left:141px;top:704px;width:120px;height:110px">
    <svg style="left:24px;top:24px" width="22" height="18" fill="#111"><use href="#i-flag"/></svg>
    <div style="left:24px;top:48px;font:600 24px 'Lexend',sans-serif">Finish</div>
  </div>
  <div class="tile" style="left:274px;top:704px;width:120px;height:110px">
    <svg style="left:24px;top:18px" width="24" height="24" color="#111"><use href="#i-route"/></svg>
    <div class="big" style="left:24px;top:44px">2.5</div><div class="unit" style="left:86px;top:50px">KM</div>
  </div>

  <div class="dark-bar" style="top:780px;height:68px">
    <div style="left:18px;top:14px;width:56px;height:40px;border:1.5px solid #999;border-radius:20px">
      <svg style="left:20px;top:12px" width="12" height="12" color="#ccc"><use href="#i-x"/></svg>
    </div>
    <div class="join" style="right:86px;top:16px">SAVE &amp;<br>PUBLISH</div>
    <div class="go" style="top:14px"><svg width="12" height="12" color="var(--accent)"><use href="#i-chev"/></svg></div>
  </div>
  <div class="home-bar"></div>
</section>
<div class="caption" style="left:860px;top:1027px">CREATE CHALLENGE</div>

<!-- ============ CHALLENGE DETAILS ============ -->
<section class="screen" style="left:338px;top:1160px">
  <div class="time">9:41</div>
  <svg class="status" width="80" height="14" fill="#111"><use href="#i-status"/></svg>
  <div class="back"><svg width="12" height="12" color="#111"><use href="#i-back"/></svg></div>
  <div class="participants" style="left:147px">32<small>PARTICIPANTS</small></div>
  <div class="share"><span>SHARE</span><svg width="22" height="22" color="var(--accent)"><use href="#i-share"/></svg></div>

  <div class="green" style="left:8px;top:144px;width:386px;height:285px">
    <div class="photo" role="img" aria-label="Marathon runner in a yellow vest" style="left:0;top:0;width:386px;height:192px;border-radius:22px;clip-path:polygon(0 0,386px 0,300px 192px,0 192px)"></div>
    <div class="title" style="left:24px;top:208px;width:330px">Downtown Up &amp; Running 3KM</div>
  </div>
  <div class="tile" style="left:8px;top:432px;width:386px;height:132px;border-radius:8px 8px 22px 22px">
    <svg style="left:24px;top:20px" width="24" height="24" color="#111"><use href="#i-route"/></svg>
    <div class="big" style="left:24px;top:48px">2.5</div><div class="unit" style="left:86px;top:50px">KM</div>
    <div class="lbl" style="left:24px;top:95px">TOTAL DISTANCE</div>
    <svg style="left:153px;top:20px" width="24" height="24" color="#111"><use href="#i-cal"/></svg>
    <div class="big" style="left:153px;top:48px">25</div><div class="unit" style="left:204px;top:50px">NOV</div>
    <div class="lbl" style="left:153px;top:95px">DAY 1</div>
    <svg style="left:265px;top:20px" width="24" height="24" color="#111"><use href="#i-clock"/></svg>
    <div class="big" style="left:265px;top:48px">9:00</div>
    <div class="lbl" style="left:265px;top:95px">START TIME</div>
  </div>

  <div class="prizes-head" style="left:16px;top:598px;width:200px;height:26px">
    <svg style="left:0;top:1px" width="24" height="24" color="#111"><use href="#i-trophy"/></svg>
    <svg style="left:28px;top:3px" width="10" height="20" stroke="var(--green)" stroke-width="3"><path d="M8 1L2 19"/></svg>
    <span style="left:44px;top:0;font:600 20px 'Lexend',sans-serif">Prizes</span>
  </div>
  <div class="tile prize" style="left:8px;top:641px;width:386px;height:86px;border-radius:18px">
    <div style="left:0;top:0;width:96px;height:86px;background:var(--dark);clip-path:polygon(0 0,96px 0,70px 86px,0 86px)"></div>
    <div style="left:24px;top:18px;font:600 22px 'Lexend',sans-serif;color:#fff">1<sup style="position:static;font-size:12px">ST</sup></div>
    <div style="left:22px;top:48px;font:400 14px 'Lexend',sans-serif;color:#fff">PLACE</div>
    <div style="left:108px;top:20px;font:500 16px 'Lexend',sans-serif">Pulse Club Premium 1 month.</div>
    <div style="left:270px;top:56px;font:500 12px 'Lexend',sans-serif">MORE INFO</div>
    <svg style="left:356px;top:57px" width="11" height="11" color="#111"><use href="#i-chev"/></svg>
  </div>
  <div class="tile prize" style="left:8px;top:737px;width:386px;height:80px;border-radius:18px">
    <div style="left:0;top:0;width:96px;height:80px;background:#555;clip-path:polygon(0 0,96px 0,70px 80px,0 80px)"></div>
    <div style="left:24px;top:16px;font:600 20px 'Lexend',sans-serif;color:#fff">2<sup style="position:static;font-size:12px">ND</sup></div>
    <div style="left:108px;top:18px;font:500 16px 'Lexend',sans-serif;color:#444">Pulse Club Premium 1 month</div>
  </div>

  <div class="dark-bar" style="top:780px;height:68px">
    <svg style="left:24px;top:22px" width="24" height="24" color="#fff"><use href="#i-timer"/></svg>
    <div class="big" style="left:50px;top:18px">1.3</div>
    <div class="unit" style="left:114px;top:20px">KM</div>
    <div class="sub" style="left:114px;top:37px">REMAINING</div>
    <div class="join" style="right:86px;top:16px">JOIN THE<br>CHALLENGE</div>
    <div class="go" style="top:14px"><svg width="12" height="12" color="var(--accent)"><use href="#i-chev"/></svg></div>
  </div>
  <div class="home-bar"></div>
</section>
<div class="caption" style="left:338px;top:2067px">CHALLENGE DETAILS</div>

<!-- ============ CHALLENGE DETAILS 2 ============ -->
<section class="screen" style="left:860px;top:1160px">
  <div class="time">9:41</div>
  <svg class="status" width="80" height="14" fill="#111"><use href="#i-status"/></svg>
  <div class="back"><svg width="12" height="12" color="#111"><use href="#i-back"/></svg></div>
  <div class="participants" style="left:147px">32<small>PARTICIPANTS</small></div>
  <div class="share"><span>SHARE</span><svg width="22" height="22" color="var(--accent)"><use href="#i-share"/></svg></div>

  <div class="green" style="left:8px;top:144px;width:386px;height:285px">
    <div class="photo" role="img" aria-label="Marathon runner in a yellow vest" style="left:0;top:0;width:386px;height:192px;border-radius:22px;clip-path:polygon(0 0,386px 0,300px 192px,0 192px)"></div>
    <div class="title" style="left:24px;top:208px;width:330px">Downtown Up &amp; Running 3KM</div>
  </div>
  <div class="tile" style="left:8px;top:432px;width:386px;height:132px;border-radius:8px 8px 22px 22px">
    <svg style="left:24px;top:20px" width="24" height="24" color="#111"><use href="#i-route"/></svg>
    <div class="big" style="left:24px;top:48px">2.5</div><div class="unit" style="left:86px;top:50px">KM</div>
    <div class="lbl" style="left:24px;top:95px">TOTAL DISTANCE</div>
    <svg style="left:153px;top:20px" width="24" height="24" color="#111"><use href="#i-cal"/></svg>
    <div class="big" style="left:153px;top:48px">25</div><div class="unit" style="left:204px;top:50px">NOV</div>
    <div class="lbl" style="left:153px;top:95px">DAY 1</div>
    <svg style="left:261px;top:20px" width="24" height="24" color="#111"><use href="#i-clock"/></svg>
    <div class="big" style="left:261px;top:48px">9:00</div>
    <div class="lbl" style="left:261px;top:95px">START TIME</div>
  </div>
  <div style="left:30px;top:564px;width:98px;height:3px;background:var(--ink)"></div>
  <div class="tile" style="left:8px;top:568px;width:386px;height:136px">
    <svg style="left:30px;top:26px" width="22" height="22" color="#111"><use href="#i-map"/></svg>
    <div style="left:61px;top:28px;font:400 13px 'Inter',sans-serif">Meadow Plaza, Linden Row ST.</div>
    <svg style="left:30px;top:61px" width="22" height="16" fill="#111"><use href="#i-flag"/></svg>
    <div style="left:61px;top:60px;font:400 13px 'Inter',sans-serif">Harbor Square, Quay RD, 2071zk.</div>
    <div style="left:322px;top:88px;width:56px;height:40px;background:#fff;border-radius:20px">
      <svg style="left:17px;top:9px" width="22" height="22" color="#111"><use href="#i-pin"/></svg>
    </div>
  </div>

  <div class="prizes-head" style="left:16px;top:734px;width:200px;height:26px">
    <svg style="left:0;top:1px" width="24" height="24" color="#111"><use href="#i-trophy"/></svg>
    <svg style="left:28px;top:3px" width="10" height="20" stroke="var(--green)" stroke-width="3"><path d="M8 1L2 19"/></svg>
    <span style="left:44px;top:0;font:600 20px 'Lexend',sans-serif">Prizes</span>
  </div>

  <div class="dark-bar" style="top:780px;height:68px">
    <svg style="left:24px;top:22px" width="24" height="24" color="#fff"><use href="#i-timer"/></svg>
    <div class="big" style="left:50px;top:18px">1.3</div>
    <div class="unit" style="left:114px;top:20px">KM</div>
    <div class="sub" style="left:114px;top:37px">REMAINING</div>
    <div class="join" style="right:86px;top:16px">JOIN THE<br>CHALLENGE</div>
    <div class="go" style="top:14px"><svg width="12" height="12" color="var(--accent)"><use href="#i-chev"/></svg></div>
  </div>
  <div class="home-bar"></div>
</section>
<div class="caption" style="left:860px;top:2067px">CHALLENGE DETAILS 2</div>

</div>
</body>
</html>
```